Business cards for Harbourline Supply Pty Ltd that import building products into Australia from China
Target Market(s)
Business to Business
Industry/Entity Type
Business
Contact Information for Business Card
Front: Logo and Business Name
Rear:
Vernon Asquill
General Manager
Mobile: 0427 196 354
email: vern@harbourlinesupply.com.au
alternative email: vern@ochrefield.com.au
web: www.harbourlinesupply.com.au
Adelaide, Brisbane and Darwin
Colors
ec1f27
fbee3d

```html
<!DOCTYPE html>
<html lang="en">
<head>
<meta charset="utf-8">
<title>Harbourline Supply – Business Cards</title>
<link rel="stylesheet" href="https://fonts.googleapis.com/css2?family=Montserrat:wght@600;800&family=Open+Sans:wght@400;600&display=swap">
<style>
  :root {
    --brand-red: #ec1f27;
    --brand-yellow: #fbee3d;
    --accent-gold: #f5c518;
    --ink-grey: #6d6e71;
    --mark-grey: #a7a9ac;
    --paper: #ffffff;
    --backdrop: #e9e9eb;
  }
  * { box-sizing: border-box; margin: 0; padding: 0; }
  html, body { width: 1200px; height: 660px; overflow: hidden; }
  body {
    background: var(--backdrop);
    font-family: "Open Sans", Arial, sans-serif;
    position: relative;
  }
  .card {
    position: absolute;
    top: 171px;
    width: 520px;
    height: 318px;
    overflow: hidden;
    box-shadow: 0 10px 28px rgba(0,0,0,.18);
  }
  .card--front { left: 50px; background: var(--brand-red); }
  .card--back  { left: 630px; background: var(--paper); }

  .front-texture { position: absolute; inset: 0; background: linear-gradient(135deg, #ef2a2f 0%, var(--brand-red) 55%, #de1820 100%); }

  .brand { position: absolute; display: flex; align-items: center; gap: 12px; }
  .brand__square { width: 44px; height: 44px; background: var(--mark-grey); flex: none; }
  .brand__name {
    font-family: "Montserrat", Arial, sans-serif;
    font-weight: 800;
    font-size: 27px;
    letter-spacing: -0.5px;
    line-height: 1;
    text-transform: uppercase;
  }
  .brand__cities {
    font-family: "Montserrat", Arial, sans-serif;
    font-weight: 600;
    font-size: 10.5px;
    letter-spacing: 1.6px;
    text-transform: uppercase;
    margin-top: 4px;
  }
  .card--front .brand { left: 70px; top: 134px; }
  .card--front .brand__name { color: var(--paper); }
  .card--front .brand__cities { color: #f6c9cb; }

  .card--back .brand { left: 26px; top: 56px; gap: 10px; }
  .card--back .brand__square { width: 38px; height: 38px; }
  .card--back .brand__name { color: var(--brand-red); font-size: 23px; }
  .card--back .brand__cities { color: var(--ink-grey); font-size: 9px; }

  .back-shapes { position: absolute; inset: 0; }

  .holder { position: absolute; right: 28px; top: 38px; text-align: right; }
  .holder__name {
    font-family: "Montserrat", Arial, sans-serif;
    font-weight: 800;
    font-size: 16px;
    color: var(--brand-red);
    text-transform: uppercase;
  }
  .holder__role { font-size: 11px; color: var(--ink-grey); margin-top: 1px; }

  .contacts { position: absolute; left: 22px; bottom: 20px; list-style: none; }
  .contacts li {
    display: flex; align-items: center; gap: 10px;
    color: var(--paper); font-size: 12.5px; line-height: 1; margin-top: 7px;
  }
  .contacts svg { width: 15px; height: 15px; flex: none; }
</style>
</head>
<body>

<section class="card card--front" aria-label="Business card front">
  <div class="front-texture" role="img" aria-label="Red background with faint large brand pattern"></div>
  <div class="brand">
    <span class="brand__square"></span>
    <div>
      <div class="brand__name">Harbourline Supply</div>
      <div class="brand__cities">Adelaide, Brisbane and Darwin</div>
    </div>
  </div>
</section>

<section class="card card--back" aria-label="Business card back">
  <svg class="back-shapes" viewBox="0 0 520 318" preserveAspectRatio="none" aria-hidden="true">
    <polygon points="0,218 520,112 520,318 0,318" fill="var(--brand-red)"/>
    <line x1="0" y1="202" x2="520" y2="96" stroke="var(--accent-gold)" stroke-width="5"/>
  </svg>

  <div class="brand">
    <span class="brand__square"></span>
    <div>
      <div class="brand__name">Harbourline Supply</div>
      <div class="brand__cities">Adelaide, Brisbane and Darwin</div>
    </div>
  </div>

  <div class="holder">
    <div class="holder__name">Vernon Asquill</div>
    <div class="holder__role">General Manager</div>
  </div>

  <ul class="contacts">
    <li>
      <svg viewBox="0 0 16 16"><rect x="4" y="1" width="8" height="14" rx="1.5" fill="none" stroke="var(--accent-gold)" stroke-width="1.6"/><circle cx="8" cy="12.5" r="0.9" fill="var(--accent-gold)"/></svg>
      0427 196 354
    </li>
    <li>
      <svg viewBox="0 0 16 16"><rect x="1" y="3" width="14" height="10" fill="var(--accent-gold)"/><polyline points="1,3 8,9 15,3" fill="none" stroke="var(--brand-red)" stroke-width="1.2"/></svg>
      vern@harbourlinesupply.com.au
    </li>
    <li>
      <svg viewBox="0 0 16 16"><rect x="1" y="3" width="14" height="10" fill="var(--accent-gold)"/><polyline points="1,3 8,9 15,3" fill="none" stroke="var(--brand-red)" stroke-width="1.2"/></svg>
      vern@ochrefield.com.au
    </li>
    <li>
      <svg viewBox="0 0 16 16"><circle cx="8" cy="8" r="6.5" fill="none" stroke="var(--accent-gold)" stroke-width="1.5"/><ellipse cx="8" cy="8" rx="2.8" ry="6.5" fill="none" stroke="var(--accent-gold)" stroke-width="1.2"/><line x1="1.5" y1="8" x2="14.5" y2="8" stroke="var(--accent-gold)" stroke-width="1.2"/></svg>
      www.harbourlinesupply.com.au
    </li>
  </ul>
</section>

</body>
</html>
```